VelgoNexus PowerPoint Design

We need a very cool power-point template done for VelgoNexus. We need it to drive the message of technology, speed and innovation. This is for a racing proposal to for our indy car team. I will attach our logo.

Target Market(s)

This presentation is for our INDY RACE CAR TEAM OVERVIEW... The Theme is: Speed, Technology and Innovation

Industry/Entity Type

Racing

Colors

Designer to choose colors to be used in the design.

Requirements
Must have
• Intro Slide with Logo - Must look very cool
Template Slide for Content
Ending Slide with something like "Thanks VelgoNexus!"
Nice to have
• Please see the example ppt deck from Morbeck a previous company to see the slide template... Also see a old template for VelgoNexus

```html
<!DOCTYPE html>
<html lang="en">
<head>
<meta charset="UTF-8">
<title>VelgoNexus — Content Slide</title>
<link rel="stylesheet" href="https://fonts.googleapis.com/css2?family=Open+Sans:wght@600;700&display=swap">
<style>
  :root {
    --navy: #062458;
    --white: #ffffff;
    --text-grey: #454545;
    --bullet-gold: #f6b21f;
    --dot-green: #8cc63f;
    --brand-blue: #38b6e8;
  }
  * { margin: 0; padding: 0; box-sizing: border-box; }
  html, body {
    width: 1200px;
    height: 900px;
    overflow: hidden;
    background: var(--white);
  }
  .slide {
    position: relative;
    width: 1200px;
    height: 900px;
    background: var(--white);
    font-family: "Open Sans", Arial, sans-serif;
  }
  .header-band {
    position: absolute;
    top: 0; left: 0;
    width: 1200px;
    height: 83px;
    background: var(--navy);
  }
  .slide-title {
    position: absolute;
    left: 26px;
    top: 16px;
    color: var(--white);
    font-size: 38px;
    font-weight: 600;
    letter-spacing: 0.5px;
    line-height: 1.2;
  }
  .header-pattern {
    position: absolute;
    top: 0; right: 0;
    width: 690px;
    height: 83px;
    background: linear-gradient(90deg, var(--navy) 0%, rgba(246,178,31,0.55) 45%, rgba(140,198,63,0.6) 75%, rgba(246,178,31,0.7) 100%);
  }
  .bullet-list {
    position: absolute;
    left: 44px;
    top: 120px;
    list-style: none;
  }
  .bullet-item {
    display: flex;
    align-items: center;
    height: 70.5px;
    color: var(--text-grey);
    font-size: 24px;
    font-weight: 700;
  }
  .bullet-dot {
    flex: none;
    width: 26px;
    height: 26px;
    border-radius: 50%;
    background: var(--bullet-gold);
    border: 4px solid var(--navy);
    margin-right: 24px;
  }
  .footer-band {
    position: absolute;
    left: 0; bottom: 0;
    width: 1200px;
    height: 105px;
    background: var(--navy);
  }
  .footer-pattern {
    position: absolute;
    left: 0; bottom: 0;
    width: 820px;
    height: 105px;
    background: linear-gradient(90deg, rgba(246,178,31,0.75) 0%, rgba(140,198,63,0.6) 40%, rgba(246,178,31,0.45) 65%, var(--navy) 100%);
  }
  .brand-name {
    position: absolute;
    right: 24px;
    bottom: 24px;
    color: var(--brand-blue);
    font-size: 34px;
    font-weight: 600;
    line-height: 1;
  }
</style>
</head>
<body>
  <main class="slide">
    <header class="header-band">
      <h1 class="slide-title">PROJECT TITLE HERE</h1>
      <div class="header-pattern" role="img" aria-label="Decorative pattern of gold and green dots"></div>
    </header>

    <ul class="bullet-list">
      <li class="bullet-item"><span class="bullet-dot"></span>Lorem ipsum dolor sit ipsum Lorem ipsum dolor sit ipsum Lorem ipsum</li>
      <li class="bullet-item"><span class="bullet-dot"></span>Lorem ipsum dolor sit ipsum Lorem ipsum dolor sit ipsum Lorem ipsum</li>
      <li class="bullet-item"><span class="bullet-dot"></span>Lorem ipsum dolor sit ipsum Lorem ipsum dolor sit ipsum Lorem ipsum</li>
      <li class="bullet-item"><span class="bullet-dot"></span>Lorem ipsum dolor sit ipsum Lorem ipsum dolor sit ipsum Lorem ipsum</li>
      <li class="bullet-item"><span class="bullet-dot"></span>Lorem ipsum dolor sit ipsum Lorem ipsum dolor sit ipsum Lorem ipsum</li>
      <li class="bullet-item"><span class="bullet-dot"></span>Lorem ipsum dolor sit ipsum Lorem ipsum dolor sit ipsum Lorem ipsum</li>
      <li class="bullet-item"><span class="bullet-dot"></span>Lorem ipsum dolor sit ipsum Lorem ipsum dolor sit ipsum Lorem ipsum</li>
      <li class="bullet-item"><span class="bullet-dot"></span>Lorem ipsum dolor sit ipsum Lorem ipsum dolor sit ipsum Lorem ipsum</li>
      <li class="bullet-item"><span class="bullet-dot"></span>Lorem ipsum dolor sit ipsum Lorem ipsum dolor sit ipsum Lorem ipsum</li>
    </ul>

    <footer class="footer-band">
      <div class="footer-pattern" role="img" aria-label="Decorative pattern of gold and green dots"></div>
      <span class="brand-name">VelgoNexus</span>
    </footer>
  </main>
</body>
</html>
```